Flyer "Pinch Analysis"-Energy Optimization procedure for Industry

We need a flyer (1xA4 recto/verso )design for a new part of our business.

In Summary: we want to communicate that we are providing "Pinch Analysis" for the industry. It's an energy optimization procedure. We are a cutting edge engineering consulting group.

All details about project in the attached files

Target Market(s)

Engineering

Industry/Entity Type

Business

Font styles to use
Serif

Requirements
Must have
• Finale document in .ai format ready for printing
• More informations in attached files
Nice to have
• See attached files

```html
<!DOCTYPE html>
<html lang="fr">
<head>
<meta charset="utf-8">
<title>Analyse Pinch – Calora</title>
<link href="https://fonts.googleapis.com/css2?family=Orbitron:wght@600;700&family=Lato:wght@400;700&family=Roboto+Condensed:wght@700&display=swap" rel="stylesheet">
<style>
  :root {
    --backdrop: #2a2a2a;
    --paper: #ffffff;
    --paper-tint: #eef5fb;
    --navy: #1c3466;
    --sky: #3db4e6;
    --sky-light: #5cc3ee;
    --yellow: #f2e23a;
    --ink: #4a4a4a;
    --ink-dark: #3a3a3a;
  }
  * { box-sizing: border-box; margin: 0; padding: 0; }
  html, body { width: 897px; height: 1200px; overflow: hidden; }
  body { background: var(--backdrop); position: relative; font-family: "Lato", sans-serif; }

  .flyer {
    position: absolute; left: 70px; top: 80px; width: 756px; height: 1060px;
    background: linear-gradient(160deg, var(--paper) 0%, var(--paper-tint) 55%, var(--paper) 100%);
    overflow: hidden;
  }
  .abs { position: absolute; }

  .header { left: 0; top: 0; width: 756px; height: 110px; background: var(--paper); }
  .header-band { left: 0; top: 92px; width: 756px; height: 14px; background: var(--sky); }
  .brand-box {
    left: 26px; top: 25px; width: 270px; height: 120px; background: var(--paper);
    border: 9px solid var(--sky); display: flex; align-items: center; justify-content: center; gap: 10px;
    z-index: 3;
  }
  .brand-mark { width: 14px; height: 14px; background: var(--sky); }
  .brand-name { font-family: "Orbitron", sans-serif; font-weight: 700; font-size: 30px; color: var(--sky); letter-spacing: 1px; }
  .headline {
    right: 22px; top: 40px; width: 440px; text-align: right;
    font-family: "Orbitron", sans-serif; font-weight: 700; font-size: 12.5px; line-height: 19px; color: var(--navy);
  }

  .hero { left: 0; top: 110px; width: 756px; height: 326px;
    background: linear-gradient(120deg, #d9dde0 0%, #9ea6ab 40%, #3c4246 70%, #c7ccd0 100%); }

  .intro-line { left: 305px; top: 440px; width: 451px; height: 10px; background: var(--sky); }
  .intro-box {
    left: 5px; top: 410px; width: 300px; height: 246px; background: var(--navy);
    padding: 14px 16px; box-shadow: 3px 4px 8px rgba(0,0,0,.25);
  }
  .intro-title { font-family: "Orbitron", sans-serif; font-weight: 700; font-size: 12px; line-height: 16px; color: var(--yellow); }
  .intro-text { margin-top: 10px; font-size: 12.5px; line-height: 15.5px; color: #fff; }

  .method { left: 320px; top: 468px; width: 415px; text-align: right; }
  .method-lead { font-family: "Roboto Condensed", sans-serif; font-weight: 700; font-size: 16.5px; line-height: 20px; color: var(--navy); }
  .method-list { list-style: none; margin-top: 6px; }
  .method-list li { position: relative; padding-right: 22px; font-size: 16px; line-height: 21px; color: var(--ink); margin-bottom: 2px; }
  .method-list li::after { content: ""; position: absolute; right: 0; top: 6px; width: 10px; height: 10px; border-radius: 50%; background: var(--navy); }

  .gallery-band { left: 0; top: 692px; width: 756px; height: 178px; background: var(--navy); }
  .gallery-frame { top: 695px; height: 143px; background: var(--paper); padding: 8px; box-shadow: 0 3px 8px rgba(0,0,0,.35); }
  .gallery-frame div { width: 100%; height: 100%; }
  .frame-1 { left: 26px; width: 219px; }
  .frame-2 { left: 271px; width: 219px; }
  .frame-3 { left: 515px; width: 231px; }
  .photo-tanks { background: linear-gradient(135deg, #2f7fc4, #8fc2e6 50%, #1f4f86); }
  .photo-pipes { background: linear-gradient(135deg, #5c6a78, #b9c2ca 50%, #3a4550); }
  .photo-sun { background: radial-gradient(circle at 60% 35%, #ffffff 0%, #9fd0f7 12%, #2f7fd8 45%, #1a54a8 100%); }

  .closing { left: 25px; top: 888px; width: 710px; font-size: 16px; line-height: 21px; font-weight: 700; color: var(--ink-dark); }
  .callout {
    left: 25px; top: 997px; width: 710px; height: 44px; background: var(--sky-light);
    color: #fff; font-size: 14px; line-height: 18px; text-align: center; padding-top: 4px;
    box-shadow: 0 2px 5px rgba(0,0,0,.2);
  }
  .footer-band { left: 0; top: 1050px; width: 756px; height: 10px; background: var(--sky); }
</style>
</head>
<body>
<main class="flyer">
  <div class="abs header"></div>
  <div class="abs header-band"></div>
  <div class="abs brand-box"><span class="brand-mark"></span><span class="brand-name">Calora</span></div>
  <h1 class="abs headline">Analyse Pinch – en route vers la performance<br>opérationnelle et l'efficacité énergétique</h1>

  <div class="abs hero" role="img" aria-label="Photo d'une chaufferie industrielle avec cuves et tuyauteries noires isolées"></div>

  <div class="abs intro-line"></div>
  <section class="abs intro-box">
    <h2 class="intro-title">La performance opérationnelle et l'efficacité énergétique sont les clés de la réussite de l'industrie de demain.</h2>
    <p class="intro-text">Fort d'une longue expérience dans l'analyse, la conception et la mise en service d'installations industrielles (chimie, alimentaire, pharmacie,…), la société Calora utilise l'analyse Pinch dans sa démarche de conception et d'amélioration.</p>
  </section>

  <section class="abs method">
    <p class="method-lead">L'analyse Pinch est une méthode d'analyse systématique développée et appliquée depuis les années 1980; elle permet de répondre aux questions suivantes:</p>
    <ul class="method-list">
      <li>Quels sont les besoins de chaleur et de froid minimaux de mon procédé</li>
      <li>Quel est mon potentiel de réduction de consommation énergétique</li>
      <li>Quel est la solution technique présentant les coûts minimaux entre investissements et économies</li>
    </ul>
  </section>

  <div class="abs gallery-band"></div>
  <div class="abs gallery-frame frame-1"><div class="photo-tanks" role="img" aria-label="Photo de réservoirs industriels bleus"></div></div>
  <div class="abs gallery-frame frame-2"><div class="photo-pipes" role="img" aria-label="Photo d'un réseau de tuyauteries métalliques"></div></div>
  <div class="abs gallery-frame frame-3"><div class="photo-sun" role="img" aria-label="Photo d'un soleil dans un ciel bleu"></div></div>

  <p class="abs closing">L'amélioration de l'efficacité énergétique est liée directement à l'exploitation des potentiels de récupération du procédé. Des potentiels de diminution de la consommation de 10 à 30% sont usuels. Nous pouvons également améliorer les performances opérationnelles en analysant vos méthodes de fabrication.</p>

  <p class="abs callout">L'analyse Pinch est aussi bien adaptée pour les PME que pour les grandes entreprises dont les procédés sont exploités de manière continue ou discontinue (batch).</p>
  <div class="abs footer-band"></div>
</main>
</body>
</html>
```